Modern business card design for professional copywriter

I'd like a business card design that I can use to have my cards printed out by plink.com as a squared corners business card (see artwork and design guidelines here: https://help.plink.com/hc/en-gb/sections/300481726-PLINK-Product-Templates)

The design should be clean and modern and reflect the colours, tone and branding on my website: https://noravestrel.com.au

Target Market(s)

Professionals, B2B small business owners

Industry/Entity Type

Business

Contact Information for Business Card

Nora Vestrel
m: 0427 593 864
e: nora@noravestrel.com.au
w: noravestrel.com.au

Font styles to use
Sans Serif

Requirements
Must have
• Tagline: "Smart copywriting for clever business people"
• Brand colours: fd8000, 009984, 666666 and black
Nice to have

```html
<!DOCTYPE html>
<html lang="en">
<head>
<meta charset="utf-8">
<title>Nora Vestrel – Business Card</title>
<link rel="stylesheet" href="https://fonts.googleapis.com/css2?family=Mulish:wght@400;700&display=swap">
<style>
  :root {
    --backdrop: #ebebeb;
    --card-white: #ffffff;
    --brand-teal: #239c86;
    --brand-orange: #f0862a;
    --text-white: #ffffff;
  }
  * { margin: 0; padding: 0; box-sizing: border-box; }
  html, body {
    width: 1200px;
    height: 1000px;
    overflow: hidden;
    background: var(--backdrop);
    font-family: "Mulish", "Century Gothic", sans-serif;
  }
  .canvas {
    position: relative;
    width: 1200px;
    height: 1000px;
  }
  .card {
    position: absolute;
  }
  .card--front {
    left: 188px;
    top: 215px;
    width: 350px;
    height: 350px;
    background: var(--card-white);
  }
  .card--back {
    left: 590px;
    top: 425px;
    width: 344px;
    height: 344px;
    background: var(--brand-teal);
  }
  .brand-name {
    position: absolute;
    left: 58px;
    top: 152px;
    display: flex;
    align-items: center;
    gap: 10px;
  }
  .brand-name__square {
    width: 14px;
    height: 14px;
    background: var(--brand-orange);
  }
  .brand-name__text {
    font-size: 30px;
    font-weight: 400;
    color: var(--brand-teal);
    letter-spacing: 0.2px;
  }
  .name-marker {
    position: absolute;
    left: 0;
    top: 137px;
    width: 23px;
    height: 29px;
    background: var(--brand-orange);
  }
  .holder-name {
    position: absolute;
    left: 32px;
    top: 140px;
    font-size: 18px;
    font-weight: 700;
    color: var(--text-white);
  }
  .contact-list {
    position: absolute;
    left: 32px;
    top: 260px;
    list-style: none;
  }
  .contact-list__item {
    display: flex;
    align-items: center;
    gap: 9px;
    height: 18.5px;
    font-size: 14px;
    color: var(--text-white);
  }
  .contact-list__icon {
    width: 14px;
    height: 14px;
    flex: none;
  }
</style>
</head>
<body>
<main class="canvas">
  <section class="card card--front" aria-label="Card front">
    <div class="brand-name">
      <span class="brand-name__square"></span>
      <span class="brand-name__text">Nora Vestrel</span>
    </div>
  </section>

  <section class="card card--back" aria-label="Card back">
    <span class="name-marker"></span>
    <h1 class="holder-name">Nora Vestrel</h1>
    <ul class="contact-list">
      <li class="contact-list__item">
        <svg class="contact-list__icon" viewBox="0 0 14 14" aria-hidden="true">
          <rect x="3.5" y="0.8" width="7" height="12.4" rx="1.2" fill="none" stroke="#f0862a" stroke-width="1.5"/>
          <rect x="5.5" y="10.2" width="3" height="1.2" fill="#f0862a"/>
        </svg>
        <span>0427 593 864</span>
      </li>
      <li class="contact-list__item">
        <svg class="contact-list__icon" viewBox="0 0 14 14" aria-hidden="true">
          <rect x="0.5" y="2.5" width="13" height="9" fill="#f0862a"/>
          <path d="M0.8 3 L7 7.8 L13.2 3" fill="none" stroke="#239c86" stroke-width="1.1"/>
        </svg>
        <span>nora@noravestrel.com.au</span>
      </li>
      <li class="contact-list__item">
        <svg class="contact-list__icon" viewBox="0 0 14 14" aria-hidden="true">
          <circle cx="7" cy="7" r="6.3" fill="#f0862a"/>
          <path d="M1 7 H13 M7 1 C4 4 4 10 7 13 M7 1 C10 4 10 10 7 13" fill="none" stroke="#239c86" stroke-width="1"/>
        </svg>
        <span>noravestrel.com.au</span>
      </li>
    </ul>
  </section>
</main>
</body>
</html>
```